We are creating the packaging for our premium gift box: “Pinewick Fairway Select.”
This box contains a green fee for two people, valid at the recipient’s choice of one of the most exclusive and scenic golf courses in Italy.
• Box dimensions: 16x16 x 2 cm
• Label coverage: The design must wrap around the two large square sides and the two lateral edges, similar to Brightcase packaging.
• Style: Elegant, refined, and modern.

Front design:
• A strong emotional golf image (luxury golf course setting, Italian landscape, or moment of play).
• Title: “Pinewick Fairway Select”.
• It must be clearly visible that the box includes a round of golf for two people in one of the 50 most exclusive and scenic golf courses in Italy.

Back design:
The back should contain the following text:

Discover Italy’s most iconic golf courses
With this gift box you and a guest can enjoy a round of golf at your choice of one of the 20 most beautiful courses in Italy. From championship layouts to breathtaking landscapes, every round is an unforgettable experience.

Some of the included courses:
• Dario Ventelli Golf Club, Rome (host of the Harlow Shield 2023)
• Grand Park Le Salvie, Turin
• Calmora Resort, Sicily
• Circolo Golf Villa Brunetta, Lake Como
• Tarsino Golf Club, Costa Smeralda
• Belmonda Golf Club, Tuscany
• Golf Club Roccalvenna, Piedmont

…and many more top-ranked Italian destinations.

How it works:
1. Choose your preferred golf course from the list.
2. Book directly with the club, using the code provided inside the box.
3. Enjoy an exclusive round of golf for two people.

This gift box offers flexibility, freedom, and access to Pinewick Fairway Select experiences — the perfect present for any passionate golfer.

The overall design should capture the prestige of Italian golf and communicate that this is the most desired gift for golf lovers.

Target Market(s)

Our target market is golf enthusiasts, gift buyers, and people looking for premium experience gifts. The typical buyer is between 30–60 years old, often purchasing for friends, family, or business partners. The gift should feel aspirational, elegant, and special — the perfect present for any golfer.

Industry/Entity Type

Gift boxes and experience packages, with a specific focus on golf and premium leisure experiences.

Font styles to use
Serif

Requirements
Must have
• A premium, elegant box design (21x21x2 cm) in line with luxury gift standards. • Emotional, high-quality golf imagery that immediately conveys the excitement of playing golf. • Clear and stylish branding of TeeParcel. • A design style inspired by Brightcase (label wrapping front + two sides + back). • On the back: a list of included golf courses and simple instructions on how to use the gift box.
Nice to have
• Minimalist and modern style with clean lines. • Touches of copper or metallic accents for a premium feel. • A contemporary design aesthetic similar to Nodal Swing or Quennark. • Lifestyle imagery that conveys joy, elegance, and aspiration, not just golf action.
Should not have
• No cheap or cluttered visuals. • No heavy use of gold or champagne tones (avoid cliché luxury). • No cartoonish or overly playful styles. • No complex text-heavy design — clarity and elegance are key.

```html
<!DOCTYPE html>
<html lang="en">
<head>
<meta charset="utf-8">
<title>Pinewick Fairway Select – Gift Box Label</title>
<link rel="stylesheet" href="https://fonts.googleapis.com/css2?family=Cinzel:wght@500&family=EB+Garamond:ital,wght@0,400;1,400&display=swap">
<style>
  :root {
    --page: #ffffff;
    --board: #2c2926;
    --edge: #141212;
    --copper: #c49a4e;
    --ink-light: #e8e3da;
    --ink-soft: #cfc8bc;
  }
  * { box-sizing: border-box; margin: 0; padding: 0; }
  html, body { width: 1200px; height: 1200px; overflow: hidden; background: var(--page); }
  .sheet {
    width: 1200px; height: 1200px;
    display: flex; justify-content: center; align-items: center; gap: 40px;
  }
  .box-face { width: 560px; }
  .label {
    position: relative; width: 560px; height: 560px;
    background: var(--board);
    overflow: hidden;
  }
  .brand {
    position: absolute; left: 48px; top: 92px;
    font-family: "Cinzel", serif; font-weight: 500;
    font-size: 32px; letter-spacing: 0.5px;
    color: var(--copper);
  }
  .photo {
    position: absolute; left: 150px; right: 28px;
  }
  .photo--front {
    top: 150px; height: 215px;
    background: linear-gradient(180deg, #2d3a86 0%, #8797c4 32%, #5f7f3a 52%, #3f7a22 75%, #22401a 100%);
  }
  .photo--back {
    top: 150px; height: 175px;
    background: linear-gradient(180deg, #9fb0b8 0%, #d9cdbf 28%, #5f7a52 50%, #8fae4a 72%, #2e4a22 100%);
  }
  .front-copy {
    position: absolute; left: 210px; top: 395px; right: 40px;
    font-family: "EB Garamond", serif; font-style: italic;
    font-size: 23px; line-height: 1.25; color: var(--ink-light);
  }
  .back-copy {
    position: absolute; left: 150px; right: 28px; top: 334px;
    font-family: "EB Garamond", serif;
    font-size: 8.6px; line-height: 1.28; color: var(--ink-soft);
  }
  .back-copy p { margin-bottom: 4px; }
  .back-copy ul, .back-copy ol { margin: 0 0 4px 12px; }
  .back-copy li { margin: 0; }
  .edge {
    height: 56px; background: var(--edge);
    display: flex; justify-content: space-around; align-items: center;
    font-family: "Cinzel", serif; font-weight: 500;
    font-size: 20px; color: var(--copper);
  }
</style>
</head>
<body>
<main class="sheet">
  <section class="box-face box-face--front">
    <div class="label">
      <div class="brand">Pinewick Fairway Select</div>
      <div class="photo photo--front" role="img" aria-label="Golf course at golden hour with an Italian villa clubhouse, umbrella pines and dramatic blue sky"></div>
      <p class="front-copy">Inside:<br>Green-Fees for a round of Golf for 2 people in one of the 20 most Exclusive &amp; Scenic Golf Courses in Italy!</p>
    </div>
    <div class="edge"><span>Pinewick Fairway Select</span><span>Pinewick Fairway Select</span></div>
  </section>

  <section class="box-face box-face--back">
    <div class="label">
      <div class="brand">Pinewick Fairway Select</div>
      <div class="photo photo--back" role="img" aria-label="Sunlit fairway among olive trees on a hillside above a coastal lagoon"></div>
      <div class="back-copy">
        <p>Discover Italy’s most iconic golf courses<br>With this gift box you and a guest can enjoy a round of golf at your choice of one of the 20 most beautiful courses in Italy. From championship layouts to breathtaking landscapes, every round is an unforgettable experience.</p>
        <p>Some of the included courses:</p>
        <ul>
          <li>Dario Ventelli Golf Club, Rome (host of the Harlow Shield 2023)</li>
          <li>Grand Park Le Salvie, Turin</li>
          <li>Calmora Resort, Sicily</li>
          <li>Circolo Golf Villa Brunetta, Lake Como</li>
          <li>Tarsino Golf Club, Costa Smeralda</li>
          <li>Belmonda Golf Club, Tuscany</li>
          <li>Golf Club Roccalvenna, Piedmont</li>
        </ul>
        <p>…and many more top-ranked Italian destinations.</p>
        <p>How it works:</p>
        <ol>
          <li>Choose your preferred golf course from the list.</li>
          <li>Book directly with the club, using the code provided inside the box.</li>
          <li>Enjoy an exclusive round of golf for two people.</li>
        </ol>
        <p>This gift box offers flexibility, freedom, and access to Pinewick Fairway Select experiences — the perfect present for any passionate golfer.</p>
      </div>
    </div>
    <div class="edge"><span>Pinewick Fairway Select</span><span>Pinewick Fairway Select</span></div>
  </section>
</main>
</body>
</html>
```